Company Broshure Oil&Energy Industry

We have recently completed a company rebranding, and our new website is now fully live and available at www.lumivarnel.ro.

To ensure consistency across all communication materials, we would like to redesign our company presentation flyer/brochure so that it fully reflects the updated branding and visual identity of the website.

Please find attached our current brochure (last item uploaded on the list), which should be redesigned in line with the new website’s look and feel. The overall structure and text content should remain unchanged; only the layout and visual design need to be updated. I have uploaded pictures from of the website theme. Can be used by designers for the new design.
Updates

We uploaded pictures belonging to website design theme that can be used for the new brochure.

Low design quality

Target Market(s)

EPC Contractors

Industry/Entity Type

Oil&Energy

Font styles to use
Other font styles liked:
• Calibri

Colors
0094D4
00A9DD
6FCCEA
C7EBF8
E9F6FB

Requirements
Must have
• a clear structure, elegant layout
Nice to have
• I would like to have a dynamic approach. To feel elegant and alive.

```html
<!DOCTYPE html>
<html lang="en">
<head>
<meta charset="utf-8">
<title>Lumivarnel Advantage Group – Company Presentation</title>
<link rel="stylesheet" href="https://fonts.googleapis.com/css2?family=Poppins:wght@400;500;600&family=Roboto:wght@400;500;700;900&display=swap">
<style>
:root{
  --stage:#9a9a9b;
  --ink:#0a0a0f;
  --navy:#0b1b2b;
  --teal:#16b4ad;
  --paper:#ffffff;
  --text-light:#e8eef2;
  --text-dark:#1c2a36;
  --row:#e4e6e8;
}
*{margin:0;padding:0;box-sizing:border-box}
html,body{width:788px;height:1200px;overflow:hidden;background:var(--stage)}
body{position:relative;font-family:"Poppins",sans-serif;color:var(--text-light)}
.slide{position:absolute;width:312px;height:241px;overflow:hidden;box-shadow:0 6px 14px rgba(0,0,0,.35)}
.dark{background:
  linear-gradient(120deg,transparent 42%,rgba(0,148,212,.55) 60%,transparent 61%),
  linear-gradient(60deg,rgba(0,120,170,.65) 0%,transparent 30%),
  var(--ink)}
.abs{position:absolute}
.head{font-family:"Roboto",sans-serif;font-weight:700;color:var(--paper)}
.head em{font-style:normal;color:var(--teal)}
.body{font-size:5.2px;line-height:1.22;color:var(--text-light)}
.photo{position:absolute}
.motto{position:absolute;left:42px;bottom:13px;font-size:3.6px;font-weight:500;color:var(--paper)}
.pill{display:inline-block;margin-top:1px;background:var(--teal);color:var(--paper);border-radius:3px;padding:0 3px;font-size:3.4px}
.partner{position:absolute;right:38px;bottom:17px;font-size:3.6px;font-weight:500;color:var(--paper)}
.page-no{position:absolute;right:6px;bottom:-6px;font-size:38px;font-weight:400;color:transparent;-webkit-text-stroke:1px var(--paper);line-height:1}
.vline{position:absolute;left:43px;top:0;height:210px;width:.6px;background:rgba(255,255,255,.35)}
.logo{font-family:"Roboto",sans-serif;font-weight:500;color:var(--paper);letter-spacing:1px}

.cover .logo{left:22px;top:22px;font-size:25px}
.cover .kicker{left:22px;top:80px;font-size:6px;letter-spacing:1.2px}
.cover .title{left:22px;top:90px;font-size:19.5px;line-height:1.15}
.cover .rule{left:22px;top:166px;width:104px;height:.6px;background:rgba(255,255,255,.4)}
.cover .tag{left:22px;top:176px;font-size:6.6px;font-family:"Roboto",sans-serif;line-height:1.35}
.cover .tag b{font-weight:700}
.cover .site{left:22px;top:216px;font-size:5.4px;letter-spacing:1.4px}
.cover .site span{color:var(--teal)}

.contact .logo{left:0;right:0;top:24px;text-align:center;font-size:22px}
.avatar{position:absolute;top:74px;width:46px;height:46px;border-radius:50%;border:1.5px solid var(--teal);padding:2px}
.avatar div{width:100%;height:100%;border-radius:50%;background:radial-gradient(circle at 50% 40%,#c9b4a6,#5b4a42)}
.contact .h{left:0;right:0;top:131px;text-align:center;font-size:10px}
.contact .icons{left:0;right:0;top:148px;display:flex;justify-content:center;gap:4px}
.contact .icons span{width:7.5px;height:7.5px;border-radius:50%;background:var(--teal);display:block}
.contact .lines{left:0;right:0;top:162px;text-align:center;font-size:6.8px;line-height:14.6px}

.svc{position:absolute;width:66px;text-align:center;font-size:4.5px;line-height:1.2}
.svc i{display:block;margin:0 auto 4px;width:26px;height:26px;border-radius:50%;background:var(--teal);box-shadow:0 0 0 2px rgba(22,180,173,.25)}
.svc i svg{width:100%;height:100%}

.industry .left{position:absolute;left:0;top:0;width:172px;height:241px}
.industry .right{position:absolute;left:172px;top:0;width:140px;height:241px;background:linear-gradient(180deg,#a9c7e2,#dfe7f2)}
.num{position:absolute;width:30px;height:30px;border-radius:50%;background:var(--navy);color:var(--paper);font-family:"Roboto",sans-serif;font-weight:900;font-size:11px;display:flex;align-items:center;justify-content:center;box-shadow:0 2px 3px rgba(0,0,0,.4)}
.ind-label{position:absolute;font-family:"Roboto",sans-serif;font-size:8px;color:#13202c}

.phases{background:linear-gradient(180deg,#cfdcec,#e9eef5)}
.phase{position:absolute;width:46px;height:46px;border-radius:5px;background:linear-gradient(160deg,#1b3247,#0a1a28);border:1px solid #b5c9da;color:var(--paper);font-size:5.2px;text-align:center;box-shadow:0 2px 4px rgba(0,0,0,.35)}
.phase i{display:block;margin:8px auto 4px;width:14px;height:14px}
.arrow{position:absolute;font-size:7px;color:var(--teal)}

.why{background:var(--paper);color:var(--text-dark)}
.stat{position:absolute;left:22px;display:flex;align-items:center;gap:6px}
.stat b{font-family:"Roboto",sans-serif;font-size:12.5px;color:var(--teal);font-weight:700}
.stat span{font-size:4.6px;font-weight:600;line-height:1.2;color:var(--text-dark)}
.sep{position:absolute;left:22px;width:115px;height:.6px;background:#8a96a0}
.refs{position:absolute;left:147px;top:0;width:143px;height:120px;background:linear-gradient(160deg,#0d5f86,#0a1a28 60%)}
.badge{position:absolute;width:27px;height:9px;border-radius:1.5px;background:var(--paper)}

.projects{background:var(--paper);color:var(--text-dark)}
table{position:absolute;left:25px;top:42px;width:267px;border-collapse:separate;border-spacing:1px 1.5px;font-size:3.6px}
th{font-family:"Roboto",sans-serif;font-size:7px;font-weight:700;color:var(--paper);height:12px;border-radius:5px 5px 0 0}
th.n{background:var(--navy)} th.t{background:var(--teal)}
td{background:var(--row);height:16px;padding:0 5px;line-height:1.15;vertical-align:middle}
td.p{font-weight:600}
.projects .motto,.projects .partner{color:var(--text-dark)}
.projects .page-no,.why .page-no{-webkit-text-stroke:1px var(--text-dark)}
</style>
</head>
<body>

<section class="slide dark cover" style="left:64px;top:65px">
  <div class="photo" role="img" aria-label="Engineer in a hard hat working at a laptop with control dashboards" style="left:130px;top:0;width:182px;height:241px;background:radial-gradient(circle at 55% 70%,rgba(230,120,40,.55),transparent 35%),radial-gradient(circle at 40% 55%,rgba(20,70,120,.8),transparent 60%),linear-gradient(200deg,rgba(0,148,212,.5),transparent 45%)"></div>
  <svg class="abs" style="left:150px;top:46px" width="66" height="66" viewBox="0 0 66 66" aria-hidden="true">
    <circle cx="33" cy="33" r="30" fill="none" stroke="rgba(255,255,255,.45)" stroke-width=".8"/>
  </svg>
  <div class="abs logo">LVG</div>
  <div class="abs kicker">COMPANY PRESENTATION</div>
  <div class="abs title head">Lumivarnel<br>Advantage<br><em style="font-weight:400">Group</em></div>
  <div class="abs rule"></div>
  <div class="abs tag">Skilled People for<br><b>Oil &amp; Energy Projects</b></div>
  <div class="abs site">www.<span>lumivarnel</span>.ro</div>
</section>

<section class="slide dark contact" style="left:407px;top:65px">
  <div class="abs logo">LVG</div>
  <div class="avatar" style="left:106px" role="img" aria-label="Portrait of contact person"><div></div></div>
  <div class="avatar" style="left:157px" role="img" aria-label="Portrait of contact person"><div></div></div>
  <div class="abs h head">Contact us</div>
  <div class="abs icons"><span></span><span></span><span></span><span></span></div>
  <div class="abs lines">0040721555018<br>office@lumivarnel.ro<br>www.lumivarnel.ro<br>Str. Exemplului, no.7 Bucharest, Romania</div>
</section>

<section class="slide dark" style="left:64px;top:336px">
  <div class="vline"></div>
  <div class="abs head" style="left:60px;top:18px;font-size:12px"><em>Who</em> we are</div>
  <div class="abs body" style="left:60px;top:46px;width:100px">
    <p>Lumivarnel Advantage Group is a Romanian registred company, founded in 2003.</p><br>
    <p>We have been active in Oil&amp;Energy industry serving local and international market by sourcing highly specilised professionals for Oil&amp;Energy projects.</p><br>
    <p>We offer a wide range of services that encompass every stage of the process, starting from the initial selection of professionals and extending to the management of employment and logistics (mobilisation) for the assigned resources. Whether the project is located domestically or abroad, we offer tailored support to ensure successful project completion for our clients.</p>
  </div>
  <div class="photo" role="img" aria-label="Refinery towers lit at sunset reflected in water" style="left:190px;top:21px;width:100px;height:172px;background:linear-gradient(180deg,#6b4a3a,#c0793a 45%,#3a2a22 70%,#b06a2e 85%,#2a1d18)"></div>
  <svg class="abs" style="left:190px;top:169px" width="24" height="24" aria-hidden="true"><polygon points="0,0 24,24 0,24" fill="#16b4ad"/></svg>
  <div class="motto">CLEAR. STEADY. PROVEN.<br><span class="pill">SINCE 2003</span></div>
  <div class="partner">SKILLED PEOPLE FOR OIL &amp; ENERGY PROJECTS</div>
  <div class="page-no">1</div>
</section>

<section class="slide dark" style="left:407px;top:336px">
  <div class="abs head" style="left:22px;top:17px;font-size:12px"><em>Services</em></div>
  <svg class="abs" style="left:0;top:0" width="312" height="241" aria-hidden="true">
    <g stroke="rgba(255,255,255,.35)" stroke-width=".6">
      <line x1="90" y1="48" x2="90" y2="127"/><line x1="157" y1="48" x2="157" y2="127"/><line x1="224" y1="48" x2="224" y2="127"/>
      <line x1="23" y1="130" x2="290" y2="130"/>
      <line x1="90" y1="133" x2="90" y2="196"/><line x1="157" y1="133" x2="157" y2="196"/><line x1="224" y1="133" x2="224" y2="196"/>
    </g>
  </svg>
  <div class="svc" style="left:22px;top:48px"><i><svg viewBox="0 0 26 26"><ellipse cx="13" cy="13" rx="7" ry="4" fill="none" stroke="#fff" stroke-width="1.4"/><circle cx="13" cy="13" r="2" fill="#fff"/></svg></i>Discipline Site Supervision (mechanical, electric, I&amp;C, piping)</div>
  <div class="svc" style="left:89px;top:48px"><i><svg viewBox="0 0 26 26"><circle cx="13" cy="10" r="3" fill="#fff"/><rect x="8" y="14" width="10" height="5" rx="1" fill="#fff"/></svg></i>Site Management (Construction/ Commissioning)</div>
  <div class="svc" style="left:157px;top:48px"><i><svg viewBox="0 0 26 26"><circle cx="13" cy="10" r="3" fill="none" stroke="#fff" stroke-width="1.4"/><path d="M7 17h8l4-2" stroke="#fff" stroke-width="1.4" fill="none"/></svg></i>Project Service Management (Planning, Cost Control/Estimate, Project Control, Document Controlling, Contract Control, Procurement)</div>
  <div class="svc" style="left:224px;top:48px"><i><svg viewBox="0 0 26 26"><circle cx="13" cy="13" r="6" fill="none" stroke="#fff" stroke-width="1.4"/><path d="M10 13l2 2 4-4" stroke="#fff" stroke-width="1.4" fill="none"/></svg></i>Quality Control, Quality Assurance</div>
  <div class="svc" style="left:22px;top:138px"><i><svg viewBox="0 0 26 26"><path d="M13 6l6 2v5c0 4-3 6-6 7-3-1-6-3-6-7V8z" fill="none" stroke="#fff" stroke-width="1.4"/><path d="M10 13l2 2 4-4" stroke="#fff" stroke-width="1.2" fill="none"/></svg></i>HSE supervision, HSE Management</div>
  <div class="svc" style="left:89px;top:138px"><i><svg viewBox="0 0 26 26"><circle cx="11" cy="9" r="2.5" fill="#fff"/><path d="M7 19l3-7h3l3 3" stroke="#fff" stroke-width="1.6" fill="none"/></svg></i>Welding &amp; NDT inspections</div>
  <div class="svc" style="left:157px;top:138px"><i><svg viewBox="0 0 26 26"><circle cx="13" cy="14" r="4" fill="none" stroke="#fff" stroke-width="1.6"/><path d="M8 8h10l-5-3z" fill="#fff"/></svg></i>Discipline Engineering (process, piping, stress piping</div>
  <div class="svc" style="left:224px;top:138px"><i><svg viewBox="0 0 26 26"><rect x="8" y="9" width="10" height="9" fill="none" stroke="#fff" stroke-width="1.4"/><path d="M11 9V6h4v3" stroke="#fff" stroke-width="1.4" fill="none"/></svg></i>Discipline Engineering (process, piping, stress piping, instrument, electric, civil)</div>
  <div class="motto">CLEAR. STEADY. PROVEN.<br><span class="pill">SINCE 2003</span></div>
  <div class="partner">SKILLED PEOPLE FOR OIL &amp; ENERGY PROJECTS</div>
  <div class="page-no">2</div>
</section>

<section class="slide industry" style="left:64px;top:607px">
  <div class="left dark"></div>
  <div class="vline"></div>
  <div class="abs head" style="left:60px;top:18px;font-size:12px;line-height:1"><em>Industry</em><br>we<br>serve</div>
  <div class="abs body" style="left:60px;top:67px;width:100px">
    <p>We are active in Oil&amp; Energy sector with hands on experience in upstream and downstream projects either brown or green field.</p><br>
    <p>Over the years we got involved in various projects within Refineries, LNG-s, Pipelines, Offshore Platforms, Power Plants (simple or combined cycle), Nuclear Power Plants and not least renewable from solar to wind or biomass. Having a large network of Romanian specialists available for mobilisation for projects inland and across the globe, we can respond quickly to clients' requests by proposing the best available resources on the market.</p>
  </div>
  <div class="motto">CLEAR. STEADY. PROVEN.<br><span class="pill">SINCE 2003</span></div>
  <div class="right"></div>
  <svg class="abs" style="left:172px;top:0" width="140" height="241" aria-hidden="true">
    <g fill="none" stroke="#16b4ad" stroke-width="6">
      <path d="M50 24 A21 21 0 0 0 42 66"/>
      <path d="M44 66 A21 21 0 0 1 50 108"/>
      <path d="M50 108 A21 21 0 0 0 42 150"/>
      <path d="M44 150 A21 21 0 0 1 50 192"/>
    </g>
  </svg>
  <div class="num" style="left:194px;top:30px">1</div>
  <div class="num" style="left:202px;top:72px">2</div>
  <div class="num" style="left:194px;top:113px">3</div>
  <div class="num" style="left:202px;top:155px">4</div>
  <div class="ind-label" style="left:232px;top:40px">Oil &amp; Gas</div>
  <div class="ind-label" style="left:240px;top:82px">Power</div>
  <div class="ind-label" style="left:232px;top:123px">Petrochemistry</div>
  <div class="ind-label" style="left:240px;top:165px">Pharma</div>
  <div class="page-no" style="-webkit-text-stroke:1px #1c2a36">3</div>
</section>

<section class="slide phases" style="left:407px;top:607px">
  <div class="photo" role="img" aria-label="Industrial chimney with steam and steel plant structures" style="left:200px;top:0;width:112px;height:241px;background:linear-gradient(90deg,rgba(207,220,236,0),#7f93a8 45%,#4f6275)"></div>
  <div class="photo" role="img" aria-label="Plant piping and steel platforms" style="left:20px;top:200px;width:180px;height:41px;background:linear-gradient(0deg,#3d4c5a,rgba(61,76,90,0))"></div>
  <div class="abs head" style="left:21px;top:17px;font-size:12px;color:#13202c"><em>Project phases</em> we cover</div>
  <div class="abs" style="left:22px;top:42px;width:150px;font-size:5.4px;line-height:1.2;color:#13202c">Lumivarnel is able to assit you along project life time by offering the key resources needed to complete and run the project.</div>
  <div class="phase" style="left:23px;top:85px"><i><svg viewBox="0 0 14 14"><circle cx="7" cy="4" r="2.5" fill="#16b4ad"/><rect x="3" y="8" width="8" height="5" fill="#16b4ad"/></svg></i>Engineering</div>
  <div class="phase" style="left:82px;top:85px"><i><svg viewBox="0 0 14 14"><rect x="3" y="4" width="8" height="9" fill="none" stroke="#16b4ad" stroke-width="1.2"/><path d="M5 4V1h4v3" stroke="#16b4ad" fill="none"/></svg></i>Construction</div>
  <div class="phase" style="left:141px;top:85px"><i><svg viewBox="0 0 14 14"><path d="M7 1l5 2v4c0 3-2 5-5 6-3-1-5-3-5-6V3z" fill="#16b4ad"/><path d="M5 7l1.5 1.5L9 6" stroke="#fff" fill="none"/></svg></i>Commissioning</div>
  <div class="phase" style="left:23px;top:147px"><i><svg viewBox="0 0 14 14"><circle cx="6" cy="3" r="2" fill="#16b4ad"/><path d="M2 13l3-7h3l3 3" stroke="#16b4ad" stroke-width="1.6" fill="none"/></svg></i>Operation</div>
  <div class="phase" style="left:82px;top:147px"><i><svg viewBox="0 0 14 14"><circle cx="7" cy="5" r="3" fill="none" stroke="#16b4ad" stroke-width="1.4"/><path d="M2 12h6l4-2" stroke="#16b4ad" stroke-width="1.2" fill="none"/></svg></i>Maintenance</div>
  <div class="phase" style="left:141px;top:147px"><i><svg viewBox="0 0 14 14"><circle cx="7" cy="8" r="3" fill="none" stroke="#16b4ad" stroke-width="1.6"/><path d="M2 3h10L7 1z" fill="#16b4ad"/></svg></i>Start-up &amp;<br>Operation</div>
  <div class="arrow" style="left:71px;top:101px">→</div>
  <div class="arrow" style="left:130px;top:101px">→</div>
  <div class="arrow" style="left:181px;top:133px">↓</div>
  <div class="arrow" style="left:130px;top:163px">←</div>
  <div class="arrow" style="left:71px;top:163px">←</div>
  <div class="page-no">4</div>
</section>

<section class="slide why" style="left:64px;top:891px">
  <div class="abs head" style="left:22px;top:17px;font-size:12px;color:#1c2a36"><em>Why</em> LVG?</div>
  <div class="stat" style="top:39px"><b>200+</b><span>Specialists deployed<br>worldwide</span></div>
  <div class="sep" style="top:58px"></div>
  <div class="stat" style="top:61px"><b>30+</b><span>Experience across 30+<br>international projects.</span></div>
  <div class="sep" style="top:80px"></div>
  <div class="abs" style="left:22px;top:85px;font-size:4.6px;font-weight:600">Efficient and cost-effective workforce solutions.</div>
  <div class="sep" style="top:96px"></div>
  <div class="abs" style="left:22px;top:102px;font-size:4.6px;font-weight:600">Flexible teams tailored to client needs.</div>
  <div class="refs">
    <div class="abs head" style="left:12px;top:17px;font-size:12px"><em>References</em></div>
    <div class="abs" style="left:12px;top:36px;width:122px;font-size:3.8px;line-height:1.25;color:var(--paper)">
      <p>Collaborations with global EPC contractors,Owners, and Engineering firms.</p><br>
      <p><span style="color:var(--teal)">Support for crucial project phases:</span> turnarounds, construction, commissioning.</p><br>
      <p><span style="color:var(--teal)">Trusted by:</span> Ferrowell, Navitas, Kalostra, Torvia, Renvalo, Strommwerk, and others.</p>
    </div>
    <div class="badge" style="left:12px;top:82px"></div>
    <div class="badge" style="left:42px;top:82px"></div>
    <div class="badge" style="left:72px;top:82px"></div>
    <div class="badge" style="left:102px;top:82px"></div>
    <div class="badge" style="left:12px;top:94px"></div>
    <div class="badge" style="left:42px;top:94px"></div>
    <div class="badge" style="left:72px;top:94px"></div>
  </div>
  <div class="photo" role="img" aria-label="Black and white industrial pipework and pumps" style="left:21px;top:121px;width:126px;height:120px;background:linear-gradient(160deg,#d8d8d8,#6a6a6a 50%,#2a2a2a)"></div>
  <div class="abs head" style="left:160px;top:131px;font-size:12px;color:#1c2a36"><em>Our</em> philosophy</div>
  <div class="abs" style="left:160px;top:149px;width:128px;font-size:3.8px;line-height:1.25;color:#1c2a36">
    <p>Daily, we realize the world is remarkably interconnected. With decades of experience, we've come to appreciate the enduring value of human relationships-much like fine wine, they grow richer with time. Through our journey, we've cultivated a robust network of more than 10K trusted professionals who rely on us just as much as we rely on them.Despite the inevitable mistakes we've made, each one served a purpose, guiding us towards improvement.</p><br>
    <p>Ultimately, it's our reputation that speaks volumes about the quality of our service.</p>
  </div>
  <div class="motto" style="left:160px;color:#1c2a36">CLEAR. STEADY. PROVEN.<br><span class="pill">SINCE 2003</span></div>
  <div class="page-no" style="right:26px">5</div>
</section>

<section class="slide projects" style="left:407px;top:891px">
  <div class="abs head" style="left:24px;top:17px;font-size:12px;color:#1c2a36"><em>Most recent</em> relevant projects</div>
  <table>
    <thead><tr><th class="n">Project</th><th class="t">Client</th><th class="n">Service</th><th class="t">Location</th></tr></thead>
    <tbody>
      <tr><td class="p">Velmora Combined Cycle Power Plant</td><td>Kalostra/Orvena Energy &amp; Metals</td><td>Commissioning Operation</td><td>Greece, Velmora 2023-2024</td></tr>
      <tr><td class="p">Kestrin Combined Cycle Power Plant</td><td>Kalostra/Orvena Energy &amp; Metals</td><td>Commissioning Operation</td><td>Slovenia, Kestrin 2024-2025</td></tr>
      <tr><td class="p">200MW gas-fired temporary emergency power plant in Harwick</td><td>Kalostra/Orvena Energy &amp; Metals</td><td>Electrical Commissioning</td><td>Ireland, Harwick Quay power plant site 2024</td></tr>
      <tr><td class="p">Dunmarra Next Generation Power Station</td><td>Torvia Montajes</td><td>Mechanical commissioning QC Supervision</td><td>Ireland, Dunmarra Bay 2024-2025</td></tr>
      <tr><td class="p">Valeni Combined Cycle Power Plant</td><td>Torvia Montajes</td><td>Mechanical Commissioning Electrical Commissioning Contract Management Loto Administration</td><td>Romania, Valeni 2024-2025</td></tr>
      <tr><td class="p">Increase Pressure in DHT Unit (IP DHT)</td><td>Ferrowell Italia</td><td>Piping Supervision Mechanical Supervision</td><td>Romania, Brazvale Refinery - owned by Danupet 2023-2025</td></tr>
      <tr><td class="p">Improve Performance of Reformer Unit (IPRU)</td><td>Ferrowell Italia</td><td>Welding/ NDT Supervision HSE Management</td><td>Romania, Brazvale Refinery owned by Danupet 2023-2025</td></tr>
      <tr><td class="p">Flare Re-Routing + NAC Tie-Ins - Ferrowell Contract 24K0517T</td><td>Ferrowell Italia</td><td>QC/ TO Engineering</td><td>Romania, Brazvale Refinery owned by Danupet 2023-2025</td></tr>
    </tbody>
  </table>
  <div class="motto" style="left:25px">CLEAR. STEADY. PROVEN.<br><span class="pill">SINCE 2003</span></div>
  <div class="partner" style="right:46px">SKILLED PEOPLE FOR OIL &amp; ENERGY PROJECTS</div>
  <div class="page-no" style="right:20px">6</div>
</section>

</body>
</html>
```